Corvane Bookkeeping Services business cards

looking for a double sided business card design. My logo is attached. I am looking for a design similar to the attached. Keen to see what my logo in white on the blue background would look like.

```html
<!DOCTYPE html>
<html lang="en">
<head>
<meta charset="UTF-8">
<title>Corvane Bookkeeping Services – Business Cards</title>
<link href="https://fonts.googleapis.com/css2?family=Poppins:wght@300;400;700;800&display=swap" rel="stylesheet">
<style>
  :root {
    --backdrop: #232323;
    --navy: #1f3a6d;
    --green: #8dbb3a;
    --white: #ffffff;
  }
  * { margin: 0; padding: 0; box-sizing: border-box; }
  html, body { width: 1200px; height: 780px; overflow: hidden; }
  body {
    background: var(--backdrop);
    font-family: "Poppins", sans-serif;
    display: flex;
    align-items: center;
    justify-content: center;
    gap: 40px;
  }
  .card {
    width: 540px;
    height: 308px;
    border-radius: 22px;
    background: var(--navy);
    position: relative;
    overflow: hidden;
    box-shadow: 0 14px 30px rgba(0,0,0,.55);
  }

  /* Front */
  .card--front { display: flex; align-items: center; justify-content: center; }
  .brand { display: flex; align-items: center; gap: 16px; }
  .brand__mark { width: 62px; height: 62px; background: var(--white); border-radius: 6px; }
  .brand__text { display: flex; flex-direction: column; }
  .brand__name { color: var(--white); font-weight: 800; font-size: 62px; line-height: 1; letter-spacing: -1px; }
  .brand__tagline { color: var(--white); font-weight: 800; font-size: 14px; letter-spacing: 3.2px; margin-top: 6px; }

  /* Back */
  .card--back { display: flex; }
  .logo-strip {
    width: 128px;
    background: var(--white);
    position: relative;
  }
  .logo-strip__inner {
    position: absolute;
    left: 50%; top: 50%;
    transform: translate(-50%, -50%) rotate(-90deg);
    display: flex; align-items: center; gap: 10px;
    white-space: nowrap;
  }
  .logo-strip__mark { width: 34px; height: 34px; background: var(--green); border-radius: 4px; }
  .logo-strip__text { display: flex; flex-direction: column; }
  .logo-strip__name { color: var(--green); font-weight: 800; font-size: 40px; line-height: 1; letter-spacing: -0.5px; }
  .logo-strip__tagline { color: var(--navy); font-weight: 800; font-size: 9px; letter-spacing: 1.9px; margin-top: 3px; }

  .details {
    flex: 1;
    padding: 42px 34px 30px 0;
    display: flex; flex-direction: column; align-items: flex-end; text-align: right;
  }
  .person__name { color: var(--green); font-size: 30px; line-height: 1.05; }
  .person__first { font-weight: 700; }
  .person__last { font-weight: 300; }
  .person__title { color: var(--white); font-size: 14px; font-weight: 400; margin-top: 2px; }
  .address { color: var(--green); font-size: 13px; font-weight: 300; line-height: 1.45; margin-top: 22px; }
  .contacts { list-style: none; margin-top: 18px; }
  .contacts li {
    color: var(--white); font-size: 13px; font-weight: 300; line-height: 1.55;
    display: flex; align-items: center; justify-content: flex-end; gap: 10px;
  }
  .contacts svg { width: 13px; height: 13px; fill: var(--green); flex: none; }
</style>
</head>
<body>

  <section class="card card--front" aria-label="Business card front">
    <div class="brand">
      <span class="brand__mark"></span>
      <div class="brand__text">
        <span class="brand__name">Corvane</span>
        <span class="brand__tagline">BOOKKEEPING SERVICES</span>
      </div>
    </div>
  </section>

  <section class="card card--back" aria-label="Business card back">
    <div class="logo-strip">
      <div class="logo-strip__inner">
        <span class="logo-strip__mark"></span>
        <div class="logo-strip__text">
          <span class="logo-strip__name">Corvane</span>
          <span class="logo-strip__tagline">BOOKKEEPING SERVICES</span>
        </div>
      </div>
    </div>

    <div class="details">
      <p class="person__name"><span class="person__first">Marta</span> <span class="person__last">Lindqvist</span></p>
      <p class="person__title">Founder &amp; CEO</p>
      <p class="address">418 Elmridge Ave. Suite 310<br>Harlow, TX 75910</p>
      <ul class="contacts">
        <li>055-210 734 618
          <svg viewBox="0 0 16 16" aria-hidden="true"><path d="M1 5c0-2 2-3 7-3s7 1 7 3v1h-3V4.5C10 4 6 4 4 4.5V6H1zM3 8l2-3h6l2 3v5H3zm5 1.2a1.5 1.5 0 1 0 0 3 1.5 1.5 0 0 0 0-3z"/></svg>
        </li>
        <li>055-210 734 619
          <svg viewBox="0 0 16 16" aria-hidden="true"><path d="M4 1h8v14H4zm1.5 1.5v9h5v-9zM8 12.5a.8.8 0 1 0 0 1.6.8.8 0 0 0 0-1.6z"/></svg>
        </li>
        <li>hello@corvanebooks.com
          <svg viewBox="0 0 16 16" aria-hidden="true"><path d="M1 4h14v9H1zm1.5 1.2V6l5.5 3.5L13.5 6v-.8L8 8.6z"/></svg>
        </li>
        <li>www.corvanebooks.com
          <svg viewBox="0 0 16 16" aria-hidden="true"><path d="M8 1a7 7 0 1 0 0 14A7 7 0 0 0 8 1zm0 1.5c.8 0 1.7 1.6 2 4H6c.3-2.4 1.2-4 2-4zM2.6 9.5h2.9c.1 1.4.4 2.6.9 3.5a5.5 5.5 0 0 1-3.8-3.5zm0-3A5.5 5.5 0 0 1 6.4 3c-.5.9-.8 2.1-.9 3.5zM8 13.5c-.8 0-1.7-1.6-2-4h4c-.3 2.4-1.2 4-2 4zm1.6-.5c.5-.9.8-2.1.9-3.5h2.9a5.5 5.5 0 0 1-3.8 3.5zm.9-6.5c-.1-1.4-.4-2.6-.9-3.5a5.5 5.5 0 0 1 3.8 3.5z"/></svg>
        </li>
      </ul>
    </div>
  </section>

</body>
</html>
```